Billboard design - consider what a billboard is

Design a billboard using my logo - Billboard is 6m x 3m
A Billboard is advertising for my company that is on a big sign.

Has to be clean and easy to read, and ideally highlights that we are Residential and Commercial builders.

Keep it clean and easy to read

The contact number for the board is

022 583 7092
www.harbourframeworks.co.nz
info@harbourframeworks.co.nz

Doesnt have to have all contact details if it doesnt fit

Has to catch peoples attention to contact us if they need a builder

Can you please change the sign to be all white writing, with black background ?
Updates

Please consider what a billboard is...

The design needs to be suitable for a billboard..

Target Market(s)

people driving past

Industry/Entity Type

Construction

Logo Text

Wellington Builder, website email address, contact number

Colors
0054AA
0677BA
7BADD7
CADEEF
E8F1F8

Requirements
Must have
• Easy to read
Nice to have
• easy to read, can clearly see contact details

```html
<!DOCTYPE html>
<html lang="en">
<head>
<meta charset="utf-8">
<title>Harbour Frameworks – Wellington Builder Billboard</title>
<link href="https://fonts.googleapis.com/css2?family=Montserrat:wght@500;600&family=Russo+One&family=Orbitron:wght@900&display=swap" rel="stylesheet">
<style>
  :root {
    --board-black: #000000;
    --brand-blue: #00a0e9;
    --soft-grey: #9a9a9a;
    --white: #ffffff;
    --canvas: #e9ecef;
  }
  html, body {
    margin: 0;
    padding: 0;
    width: 1200px;
    height: 400px;
    overflow: hidden;
    background: var(--canvas);
  }
  .billboard {
    position: absolute;
    left: 200px;
    top: 0;
    width: 800px;
    height: 400px;
    overflow: hidden;
    background: var(--board-black);
    color: var(--white);
    font-family: "Montserrat", sans-serif;
  }
  .swoosh-layer {
    position: absolute;
    inset: 0;
  }
  .brand-mark {
    position: absolute;
    left: 34px;
    top: 58px;
    display: flex;
    align-items: center;
    gap: 14px;
  }
  .brand-square {
    width: 20px;
    height: 92px;
    background: var(--brand-blue);
  }
  .brand-name {
    margin: 0;
    color: var(--white);
    font-weight: 600;
    font-size: 34px;
    line-height: 1.15;
  }
  .divider {
    position: absolute;
    left: 318px;
    top: 40px;
    width: 3px;
    height: 128px;
    background: var(--white);
  }
  .headline {
    position: absolute;
    left: 330px;
    top: 50px;
    width: 460px;
    margin: 0;
    text-align: center;
    color: var(--white);
    font-family: "Russo One", sans-serif;
    font-weight: 400;
    line-height: 1;
  }
  .headline-place {
    display: block;
    font-size: 50px;
    letter-spacing: 2px;
  }
  .headline-trade {
    display: block;
    margin-top: 8px;
    font-size: 42px;
    letter-spacing: 9px;
  }
  .services {
    position: absolute;
    left: 0;
    top: 186px;
    width: 800px;
    margin: 0;
    text-align: center;
    color: var(--white);
    font-family: "Orbitron", sans-serif;
    font-weight: 900;
    font-size: 17px;
    letter-spacing: 6px;
    white-space: nowrap;
  }
  .email {
    position: absolute;
    left: 0;
    top: 222px;
    width: 800px;
    margin: 0;
    text-align: center;
    color: var(--white);
    font-weight: 500;
    font-size: 26px;
    white-space: nowrap;
  }
  .contact-row {
    position: absolute;
    left: 0;
    width: 800px;
    display: flex;
    align-items: center;
    justify-content: center;
    gap: 14px;
    color: var(--white);
    font-weight: 500;
    white-space: nowrap;
    line-height: 1;
  }
  .contact-phone { top: 296px; font-size: 44px; }
  .contact-web { top: 352px; font-size: 28px; }
  .contact-icon {
    display: flex;
    align-items: center;
    justify-content: center;
    background: var(--white);
  }
  .contact-phone .contact-icon { width: 40px; height: 40px; }
  .contact-web .contact-icon { width: 30px; height: 30px; }
</style>
</head>
<body>
<div class="billboard">
  <svg class="swoosh-layer" width="800" height="400" viewBox="0 0 800 400" aria-hidden="true">
    <defs>
      <linearGradient id="fadeBlue" x1="0" y1="0" x2="1" y2="0">
        <stop offset="0" stop-color="#00a0e9" stop-opacity="0"/>
        <stop offset="1" stop-color="#00a0e9" stop-opacity="0.85"/>
      </linearGradient>
    </defs>
    <path d="M0,236 Q300,280 800,270 L800,290 Q330,296 0,262 Z" fill="url(#fadeBlue)"/>
    <path d="M0,262 Q330,296 800,284 L800,400 L0,400 Z" fill="var(--brand-blue)"/>
    <path d="M150,262 Q460,282 800,262 L800,274 Q460,290 150,262 Z" fill="var(--soft-grey)"/>
  </svg>

  <div class="brand-mark">
    <div class="brand-square"></div>
    <h1 class="brand-name">Harbour<br>Frameworks</h1>
  </div>

  <div class="divider"></div>

  <h2 class="headline">
    <span class="headline-place">WELLINGTON</span>
    <span class="headline-trade">BUILDER</span>
  </h2>

  <p class="services">RESIDENTIAL AND COMMERCIAL</p>

  <p class="email">info@harbourframeworks.co.nz</p>

  <div class="contact-row contact-phone">
    <span class="contact-icon">
      <svg width="28" height="28" viewBox="0 0 24 24" aria-hidden="true">
        <path fill="#00a0e9" d="M6.6 10.8c1.4 2.8 3.8 5.1 6.6 6.6l2.2-2.2c.3-.3.7-.4 1-.2 1.1.4 2.3.6 3.6.6.6 0 1 .4 1 1V20c0 .6-.4 1-1 1C10.6 21 3 13.4 3 4c0-.6.4-1 1-1h3.5c.6 0 1 .4 1 1 0 1.3.2 2.5.6 3.6.1.3 0 .7-.2 1z"/>
      </svg>
    </span>
    <span class="contact-text">022 583 7092</span>
  </div>

  <div class="contact-row contact-web">
    <span class="contact-icon">
      <svg width="22" height="22" viewBox="0 0 24 24" aria-hidden="true">
        <circle cx="12" cy="12" r="10" fill="none" stroke="#00a0e9" stroke-width="2"/>
        <ellipse cx="12" cy="12" rx="4.5" ry="10" fill="none" stroke="#00a0e9" stroke-width="1.6"/>
        <line x1="2" y1="12" x2="22" y2="12" stroke="#00a0e9" stroke-width="1.6"/>
      </svg>
    </span>
    <span class="contact-text">www.harbourframeworks.co.nz</span>
  </div>
</div>
</body>
</html>
```